Tennis Club Brunnwil - Join the journey!

Our tennis club has fallen asleep in the past 10 years and the amount of members steadily decreased. We are now a new crew of motivated players that want to bring change, good atmosphere with up to date offers to our members.
For this specific part, we are looking to attract new adult members with different training offers.
We need one flyer that we want to use for multiple occasions:
- in 2-3 versions (different colour scheme or slightly different setup of the elements)
- A sample text inserted that we can modify later on

Our current logo and home made flyer look dusty instead of sexy. We are looking for a fresh, attractive and dynamic flyer that makes people want to be part of our activities. Our club is located in German-speaking part of Switzerland. The homepage is https://tcbrunnwil.example/ .
I attached two files:
1. The logo: Looks old school, but it necessarily needs to be part of the flyer. Use any effect you want on it to make it look more attractive.
2. The super tennis bee: This bee can be used as inspiration, but it is purely optional. It was drawn close to our club house in the early 2000s and is used as a ball-wall.

Target Market(s)

Requirements
Must have
• - in 3 versions (different colour scheme or slightly different setup of the elements)
- The logo: Looks old school, but it necessarily needs to be part of the flyer. Use any effect you want on it to make it look more attractive.
Nice to have
• The super tennis bee: This bee can be used as inspiration, but it is purely optional. It was drawn close to our club house in the early 2000s and is used as a ball-wall

```html
<!DOCTYPE html>
<html lang="en">
<head>
<meta charset="utf-8">
<title>Tennis Club Brunnwil – Training Camp</title>
<link rel="stylesheet" href="https://fonts.googleapis.com/css2?family=Montserrat:wght@400;500;700;800&display=swap">
<style>
  :root {
    --bg-dark: #1f1f1f;
    --yellow: #f5cd2c;
    --white: #ffffff;
    --ink: #1c1c1c;
    --cream: #f3f1dc;
    --body-text: #f2f2f2;
  }
  * { margin: 0; padding: 0; box-sizing: border-box; }
  html, body { width: 848px; height: 1200px; overflow: hidden; background: var(--bg-dark); }
  .flyer {
    position: relative;
    width: 848px;
    height: 1200px;
    overflow: hidden;
    font-family: "Montserrat", sans-serif;
    background:
      radial-gradient(ellipse 260px 420px at 640px 470px, rgba(111,118,112,0.85) 0%, rgba(70,74,71,0.5) 45%, rgba(31,31,31,0) 100%),
      linear-gradient(180deg, #242424 0%, #1d1d1d 100%);
  }
  .players-photo {
    position: absolute;
    z-index: 1;
    left: 492px;
    top: 140px;
    width: 310px;
    height: 832px;
    border-radius: 6px;
    background: linear-gradient(165deg, #3a5fae 0%, #2a4f9e 40%, #a9c8e8 62%, #e8e8e6 85%, #3a3a3a 100%);
    opacity: 0.85;
  }
  .club-mark {
    position: absolute;
    z-index: 2;
    left: 72px;
    top: 170px;
    display: flex;
    align-items: center;
    gap: 10px;
    color: var(--cream);
    font-weight: 800;
    font-size: 26px;
    letter-spacing: 1px;
    white-space: nowrap;
  }
  .club-mark .dot {
    width: 22px; height: 22px; border-radius: 50%;
    background: var(--cream);
    flex: none;
  }
  .headline {
    position: absolute;
    z-index: 2;
    left: 52px;
    top: 362px;
    font-weight: 800;
    line-height: 1;
    letter-spacing: -2px;
    white-space: nowrap;
  }
  .headline .line-1 { display: block; color: var(--white); font-size: 84px; }
  .headline .line-2 { display: block; color: var(--yellow); font-size: 104px; margin-top: -2px; }
  .tag {
    position: absolute;
    z-index: 2;
    left: 54px;
    top: 573px;
    height: 38px;
    padding: 0 9px;
    background: var(--yellow);
    color: var(--ink);
    font-weight: 700;
    font-size: 31px;
    line-height: 38px;
    letter-spacing: 0.8px;
    white-space: nowrap;
  }
  .intro {
    position: absolute;
    z-index: 2;
    left: 60px;
    top: 648px;
    width: 367px;
    color: var(--body-text);
    font-weight: 500;
    font-size: 20.5px;
    letter-spacing: 0.4px;
    line-height: 33.4px;
    text-align: justify;
  }
  .highlight {
    position: absolute;
    z-index: 2;
    left: 63px;
    top: 933px;
    color: var(--yellow);
    font-weight: 700;
    font-size: 19.5px;
    white-space: nowrap;
  }
  .cta {
    position: absolute;
    left: 0;
    top: 1050px;
    width: 848px;
    text-align: center;
    font-weight: 700;
    font-size: 30px;
    color: var(--white);
    letter-spacing: -0.5px;
    white-space: nowrap;
  }
  .cta .divider {
    display: inline-block;
    width: 1.5px; height: 22px;
    background: var(--white);
    margin: 0 22px;
    vertical-align: -2px;
  }
  .cta .phone { color: var(--yellow); }
  .website {
    position: absolute;
    left: 0;
    top: 1113px;
    width: 848px;
    text-align: center;
    color: var(--white);
    font-weight: 700;
    font-size: 13px;
    letter-spacing: 7.5px;
  }
</style>
</head>
<body>
<main class="flyer">
  <div class="players-photo" role="img" aria-label="Photo of two smiling tennis players holding rackets, a man in a blue shirt and a woman in a light blue top and white skirt"></div>

  <div class="club-mark"><span class="dot"></span>TC BRUNNWIL</div>

  <h1 class="headline">
    <span class="line-1">ARE YOU</span>
    <span class="line-2">READY?</span>
  </h1>

  <div class="tag">TRAINING CAMP</div>

  <p class="intro">Lorem ipsum dolor sit amet, consectetur adipiscing elit, sed do eiusmod tempor incididunt ut labore et dolore magna aliqua. Quis ipsum suspendisse ultrices gravida. Risus commodo viverra maecenas accumsan lacus vel facilisis.</p>

  <p class="highlight">LOREM IPSUM DOLOR SIT AMET</p>

  <p class="cta">JOIN NOW<span class="divider"></span>CALL <span class="phone">1800 555 321</span></p>
  <p class="website">WWW.CLUBNAME.COM</p>
</main>
</body>
</html>
```